Trifold brochure

Need a trifold marketing brochure for my autism therapy for children business . I would be interested in having designs in both English and Spanish if possible!!!!! Website is www.meadowlarkcareaba.com
Address on brochure needs to be 2718 Tamarind Ave W Suite 5
Brinwood, MN 55192
Updates
Can you update the address on brochure to 2718 Tamarind Ave W Suite 5
Brinwood, MN 55192
Target Market(s)
Autism therapy for children
Industry/Entity Type
Autism Therapy
Look and feel
Each slider illustrates characteristics of the customer's brand and the style your logo design should communicate.

```html
<!DOCTYPE html>
<html lang="en">
<head>
<meta charset="utf-8">
<title>Meadowlark Care Behavioral Therapy – Trifold Brochure</title>
<link rel="stylesheet" href="https://fonts.googleapis.com/css2?family=Merriweather:ital,wght@0,700;0,900;1,400&family=Montserrat:wght@400;500;600&display=swap">
<style>
  :root{
    --navy:#0d5596;
    --blue:#12609f;
    --band:#0f4f8c;
    --sky:#2f88cc;
    --ink:#2c2c2c;
    --white:#ffffff;
    --stage:#a3a3a3;
  }
  *{box-sizing:border-box;margin:0;padding:0}
  html,body{width:803px;height:1200px;overflow:hidden;background:var(--stage)}
  body{font-family:"Montserrat",sans-serif;color:var(--ink);position:relative}
  .spread{position:absolute;left:16px;width:771px;height:546px;background:var(--white);overflow:hidden;box-shadow:0 2px 8px rgba(0,0,0,.25)}
  .spread--outside{top:36px}
  .spread--inside{top:618px}
  .waves{position:absolute;inset:0;width:771px;height:546px}
  .panel{position:absolute;top:0;width:257px;height:546px}
  .panel--left{left:0}.panel--mid{left:257px}.panel--right{left:514px}
  h2.section{font-family:"Merriweather",serif;font-weight:700;font-size:10.5px;color:var(--navy);padding-bottom:4px;position:relative;margin-bottom:8px}
  h2.section::after{content:"";position:absolute;left:0;bottom:0;width:28px;height:1.5px;background:var(--navy)}
  p.body{font-size:6.6px;line-height:1.5;color:var(--ink)}
  .photo{position:absolute}
  .approach{position:absolute;left:26px;top:26px;width:210px}
  .approach strong{color:var(--navy)}
  .check-item{display:flex;gap:10px;margin-top:12px}
  .check-item svg{flex:0 0 22px}
  .check-item h3{font-family:"Merriweather",serif;font-size:7.4px;color:var(--navy);font-weight:700;margin-bottom:2px}
  .check-item p{font-size:6.2px;line-height:1.4}
  .logo{text-align:center;color:var(--navy);font-family:"Montserrat",sans-serif;font-weight:600}
  .logo .dot{display:block;margin:0 auto 8px;width:34px;height:34px;border-radius:50%;background:var(--navy)}
  .logo .name{display:block;font-size:19px;letter-spacing:.3px;line-height:1.05}
  .logo .sub{display:block;font-size:10.2px;letter-spacing:.4px;margin-top:3px}
  .logo--small .dot{width:26px;height:26px;margin-bottom:6px}
  .logo--small .name{font-size:14.5px}
  .logo--small .sub{font-size:8px}
  .mid-top{position:absolute;left:0;width:257px;top:34px}
  .cta{text-align:center;margin-top:34px;padding:0 24px}
  .cta .kicker{font-family:"Merriweather",serif;font-style:italic;font-size:6.8px;margin-bottom:6px}
  .cta h1{font-family:"Merriweather",serif;font-weight:900;font-size:15px;line-height:1.2;color:var(--navy)}
  .contact{position:absolute;left:30px;top:362px;width:200px;color:var(--white)}
  .pill{display:block;text-align:center;border-radius:12px;background:var(--sky);color:var(--white);font-weight:600;font-size:8.2px;padding:4px 0}
  .contact ul{list-style:none;margin-top:12px}
  .contact li{display:flex;align-items:flex-start;gap:8px;font-size:7.4px;line-height:1.35;margin-bottom:11px}
  .contact li svg{flex:0 0 9px;margin-top:1px}
  .socials{display:flex;align-items:center;justify-content:center;gap:4px;margin-top:4px}
  .socials .rule{width:48px;height:1px;background:var(--white);margin:0 6px}
  .socials .dot{width:10px;height:10px;border-radius:50%;background:var(--white)}
  .cover-top{position:absolute;left:0;top:34px;width:257px}
  .cover-copy{position:absolute;left:18px;top:375px;width:221px;text-align:center;color:var(--white)}
  .cover-copy h1{font-family:"Merriweather",serif;font-weight:900;font-size:17px;line-height:1.25}
  .cover-copy p{font-size:6.7px;line-height:1.45;margin:8px 0 14px}
  .pill--url{font-family:"Merriweather",serif;font-weight:700;font-size:9.5px;padding:5px 0;border-radius:14px}
  .about{position:absolute;left:26px;top:240px;width:212px}
  .about h2.section+p{margin-bottom:18px}
  .value{position:absolute;left:22px;top:26px;width:215px}
  .value .kicker{font-family:"Merriweather",serif;font-style:italic;font-size:7.4px;color:var(--navy)}
  .value h2.section{font-size:9.6px}
  .pillar{display:flex;gap:10px;margin-top:12px;padding-left:6px}
  .pillar .icon{flex:0 0 32px;height:32px;border-radius:50%;background:var(--navy);display:flex;align-items:center;justify-content:center}
  .pillar h3{font-family:"Merriweather",serif;font-size:7.6px;color:var(--navy);font-weight:700;margin-bottom:1px}
  .pillar p{font-size:6.3px;line-height:1.4}
  .value .pill--url{margin:18px 8px 0;background:var(--navy)}
  .services{position:absolute;left:22px;top:26px;width:218px;color:var(--white)}
  .services h2{font-family:"Merriweather",serif;font-weight:700;font-size:10.5px;padding-bottom:4px;position:relative;margin-bottom:12px}
  .services h2::after{content:"";position:absolute;left:0;bottom:0;width:28px;height:1.5px;background:var(--white)}
  .service{display:flex;gap:8px;margin-bottom:11px}
  .service svg{flex:0 0 9px;margin-top:2px}
  .service h3{font-family:"Merriweather",serif;font-size:7.4px;font-weight:700;margin-bottom:2px;line-height:1.3}
  .service p{font-size:6.2px;line-height:1.4}
</style>
</head>
<body>

<section class="spread spread--outside">
  <div class="photo" role="img" aria-label="Photo of a therapist reading a picture book with a young boy at a table" style="left:514px;top:118px;width:257px;height:230px;background:linear-gradient(135deg,#e9e4dc,#d7c8b8 45%,#b9c7d3)"></div>
  <svg class="waves" viewBox="0 0 771 546" aria-hidden="true">
    <defs>
      <linearGradient id="momPhoto" x1="0" y1="0" x2="1" y2="1">
        <stop offset="0" stop-color="#e2b07a"/><stop offset=".5" stop-color="#9a6a4c"/><stop offset="1" stop-color="#3f6f9e"/>
      </linearGradient>
    </defs>
    <path d="M0 322 C180 300 420 300 771 292 L771 546 L0 546Z" fill="var(--band)"/>
    <path d="M0 330 C200 306 420 312 771 318" fill="none" stroke="var(--white)" stroke-width="5"/>
    <path d="M0 345 C200 318 430 322 771 332" fill="none" stroke="var(--sky)" stroke-width="3"/>
    <path d="M0 356 C100 350 190 346 257 344 L257 546 L0 546Z" fill="url(#momPhoto)" role="img" aria-label="Photo of a smiling mother and young son sharing a laugh"/>
  </svg>

  <div class="panel panel--left">
    <div class="approach">
      <h2 class="section">Our Approach</h2>
      <p class="body">At Meadowlark Care, we take a holistic approach to autism therapy, recognizing that each child is unique. Our services are tailored to address the specific needs of children with autism spectrum disorder (ASD). <strong>Here’s what sets us apart:</strong></p>
      <div class="check-item">
        <svg width="22" height="22" viewBox="0 0 22 22"><circle cx="11" cy="11" r="9.5" fill="none" stroke="var(--navy)" stroke-width="2"/><path d="M6.5 11.2l3 3 6-6" fill="none" stroke="var(--navy)" stroke-width="2"/></svg>
        <div><h3>Early Intervention</h3><p>Our programs focus on early detection, assessment, and intervention to maximize developmental gains during critical periods.</p></div>
      </div>
      <div class="check-item">
        <svg width="22" height="22" viewBox="0 0 22 22"><circle cx="11" cy="11" r="9.5" fill="none" stroke="var(--navy)" stroke-width="2"/><path d="M6.5 11.2l3 3 6-6" fill="none" stroke="var(--navy)" stroke-width="2"/></svg>
        <div><h3>Individualized Treatment Plans</h3><p>Our experienced therapists create personalized treatment plans based on each child’s strengths, challenges, and developmental goals.</p></div>
      </div>
      <div class="check-item">
        <svg width="22" height="22" viewBox="0 0 22 22"><circle cx="11" cy="11" r="9.5" fill="none" stroke="var(--navy)" stroke-width="2"/><path d="M6.5 11.2l3 3 6-6" fill="none" stroke="var(--navy)" stroke-width="2"/></svg>
        <div><h3>Safe and Supportive Environment</h3><p>Our therapy spaces are designed to be calming and sensory-friendly. We create a nurturing environment where children feel comfortable exploring and learning.</p></div>
      </div>
    </div>
  </div>

  <div class="panel panel--mid">
    <div class="mid-top">
      <div class="logo"><span class="dot"></span><span class="name">MEADOWLARK CARE</span><span class="sub">BEHAVIORAL THERAPY</span></div>
      <div class="cta">
        <p class="kicker">Ready to Take the Next Step?</p>
        <h1>Contact Us Today for Expert Autism Therapy Services!</h1>
      </div>
    </div>
    <div class="contact">
      <span class="pill">Get In Touch</span>
      <ul>
        <li><svg width="9" height="9" viewBox="0 0 10 10"><path d="M2 1l2 2-1 1.3c.6 1.2 1.5 2.1 2.7 2.7L7 6l2 2-1.2 1.3C4.5 9 1 5.5.7 2.2Z" fill="var(--white)"/></svg>555-014-0148</li>
        <li><svg width="9" height="11" viewBox="0 0 10 12"><path d="M5 0a4 4 0 0 1 4 4c0 3-4 8-4 8S1 7 1 4a4 4 0 0 1 4-4Z" fill="var(--white)"/><circle cx="5" cy="4" r="1.5" fill="var(--band)"/></svg>2718 Tamarind Ave W Suite 5<br>Brinwood, MN 55192</li>
        <li><svg width="9" height="9" viewBox="0 0 10 10"><circle cx="5" cy="5" r="5" fill="var(--white)"/><rect x="2.3" y="3.2" width="5.4" height="3.6" fill="none" stroke="var(--band)" stroke-width=".8"/><path d="M2.3 3.2 5 5.3 7.7 3.2" fill="none" stroke="var(--band)" stroke-width=".8"/></svg>info@meadowlarkcareaba.com</li>
        <li><svg width="9" height="9" viewBox="0 0 10 10"><circle cx="5" cy="5" r="5" fill="var(--white)"/><circle cx="5" cy="5" r="2.8" fill="none" stroke="var(--band)" stroke-width=".7"/><path d="M2.2 5h5.6M5 2.2v5.6" stroke="var(--band)" stroke-width=".6"/></svg>meadowlarkcareaba.com</li>
      </ul>
      <div class="socials"><span class="rule"></span><span class="dot"></span><span class="dot"></span><span class="dot"></span><span class="rule"></span></div>
    </div>
  </div>

  <div class="panel panel--right">
    <div class="cover-top">
      <div class="logo logo--small"><span class="dot"></span><span class="name">MEADOWLARK CARE</span><span class="sub">BEHAVIORAL THERAPY</span></div>
    </div>
    <div class="cover-copy">
      <h1>Building Bridges to Brighter Futures</h1>
      <p>Discovering the Unique Potential of Every Child through Compassionate, Evidence-Based Autism Therapy, Fostering Growth, Connection, and Confidence.</p>
      <span class="pill pill--url">meadowlarkcareaba.com</span>
    </div>
  </div>
</section>

<section class="spread spread--inside">
  <svg class="waves" viewBox="0 0 771 546" aria-hidden="true">
    <defs>
      <linearGradient id="girlsPhoto" x1="0" y1="0" x2="1" y2="1">
        <stop offset="0" stop-color="#ece9e6"/><stop offset=".5" stop-color="#c9b29c"/><stop offset="1" stop-color="#d9dde3"/>
      </linearGradient>
      <linearGradient id="hugPhoto" x1="0" y1="0" x2="1" y2="1">
        <stop offset="0" stop-color="#5b4a3f"/><stop offset="1" stop-color="#9bb58a"/>
      </linearGradient>
      <linearGradient id="puzzlePhoto" x1="0" y1="0" x2="1" y2="0">
        <stop offset="0" stop-color="#c9dcef"/><stop offset=".5" stop-color="#d9d2e8"/><stop offset="1" stop-color="#c5d9ee"/>
      </linearGradient>
    </defs>
    <rect x="0" y="0" width="257" height="222" fill="url(#girlsPhoto)" role="img" aria-label="Photo of two little girls playing with puzzle pieces at a table"/>
    <circle cx="180" cy="176" r="56" fill="url(#hugPhoto)" stroke="var(--white)" stroke-width="4" role="img" aria-label="Photo of a mother hugging her young son"/>
    <path d="M514 0 H771 V352 C690 356 600 366 514 382Z" fill="var(--band)"/>
    <path d="M257 418 C400 378 590 356 771 348" fill="none" stroke="var(--navy)" stroke-width="9"/>
    <path d="M257 430 C400 392 590 370 771 362" fill="none" stroke="var(--white)" stroke-width="4"/>
    <path d="M257 440 C400 402 590 380 771 372 L771 546 L257 546Z" fill="url(#puzzlePhoto)" role="img" aria-label="Photo of many hands raising colourful puzzle pieces against a pale sky"/>
  </svg>

  <div class="panel panel--left">
    <div class="about">
      <h2 class="section">About ABA Therapy</h2>
      <p class="body">ABA Therapy Applied Behavioral Analysis (ABA) Therapy is endorsed by the National Child Health Council and the Regional Pediatric Care Alliance and has been scientifically proven to be the most effective in helping a child with autism to acquire the necessary skills to reach their full potential. Research has proven that early diagnosis and intervention are key to achieving success, as well as a commitment to the individualized treatment plan developed specifically for your child by one of our expert Clinicians.</p>
      <h2 class="section">How We Do ABA Therapy</h2>
      <p class="body">Meadowlark Care offers a safe and clean center-based environment, led by highly-trained clinicians. Our team of experienced Certified Behavior Specialists (CBS) and Registered Therapy Technicians work with you and your child to develop individualized treatment plans based on their unique needs.</p>
    </div>
  </div>

  <div class="panel panel--mid">
    <div class="value">
      <p class="kicker">Our Value</p>
      <h2 class="section">Quality Care From Quality Experts.</h2>
      <p class="body">At Meadowlark Care, our values drive our mission. We provide compassionate, evidence-based therapy for children with autism, focusing on individualized care and early intervention in a nurturing environment.</p>
      <div class="pillar">
        <span class="icon"><svg width="18" height="12" viewBox="0 0 18 12"><path d="M1 6C4 1 14 1 17 6 14 11 4 11 1 6Z" fill="var(--white)"/><circle cx="9" cy="6" r="3" fill="var(--navy)"/></svg></span>
        <div><h3>Vision</h3><p>To envision and strive towards a future where every child diagnosed with autism is supported, empowered, and equipped to achieve their fullest potential, fostering inclusivity and acceptance.</p></div>
      </div>
      <div class="pillar">
        <span class="icon"><svg width="18" height="18" viewBox="0 0 18 18"><circle cx="9" cy="9" r="7.5" fill="none" stroke="var(--white)" stroke-width="1.5"/><circle cx="9" cy="9" r="4.5" fill="none" stroke="var(--white)" stroke-width="1.5"/><circle cx="9" cy="9" r="1.6" fill="var(--white)"/><path d="M9 9 16 2" stroke="var(--white)" stroke-width="1.3"/></svg></span>
        <div><h3>Mission</h3><p>We’re dedicated to providing personalized, evidence-based therapy for every child with autism. Through early intervention and compassionate care, we empower growth and confidence, fostering thriving futures.</p></div>
      </div>
      <div class="pillar">
        <span class="icon"><svg width="16" height="16" viewBox="0 0 16 16"><rect x="3" y="2" width="10" height="12" rx="1" fill="var(--white)"/><path d="M5 6h6M5 8.5h6M5 11h4" stroke="var(--navy)" stroke-width="1"/></svg></span>
        <div><h3>Motto</h3><p>Unlocking Potential, Building Bridges, Illuminating Futures: Together, We Build Brighter Tomorrows.</p></div>
      </div>
      <span class="pill pill--url">meadowlarkcareaba.com</span>
    </div>
  </div>

  <div class="panel panel--right">
    <div class="services">
      <h2>Our Services</h2>
      <div class="service">
        <svg width="9" height="8" viewBox="0 0 9 8"><path d="M1 4.2 3.4 6.5 8 1" fill="none" stroke="var(--white)" stroke-width="1.8"/></svg>
        <div><h3>Applied Behavior Analysis<br>(ABA) Therapy</h3><p>Our ABA therapy focuses on enhancing communication, social skills, and behavior management in children with autism spectrum disorder (ASD).</p></div>
      </div>
      <div class="service">
        <svg width="9" height="8" viewBox="0 0 9 8"><path d="M1 4.2 3.4 6.5 8 1" fill="none" stroke="var(--white)" stroke-width="1.8"/></svg>
        <div><h3>Speech and Language Therapy</h3><p>Our speech and language therapy services aim to improve communication, expressive language, and social interaction abilities in children with autism. Using tailored approaches and innovative techniques</p></div>
      </div>
      <div class="service">
        <svg width="9" height="8" viewBox="0 0 9 8"><path d="M1 4.2 3.4 6.5 8 1" fill="none" stroke="var(--white)" stroke-width="1.8"/></svg>
        <div><h3>Occupational Therapy (OT)</h3><p>Occupational therapy at Meadowlark Care targets the development of fine motor skills, sensory processing abilities, and self-care capabilities in children with autism. Through engaging activities and individualized interventions, our occupational therapists help children build essential life skills and gain independence in daily activities.</p></div>
      </div>
      <div class="service">
        <svg width="9" height="8" viewBox="0 0 9 8"><path d="M1 4.2 3.4 6.5 8 1" fill="none" stroke="var(--white)" stroke-width="1.8"/></svg>
        <div><h3>Social Skills Training</h3><p>Our social skills training programs focus on teaching crucial social skills to children with autism, enabling them to navigate social interactions confidently. Through structured group activities and personalized coaching.</p></div>
      </div>
    </div>
  </div>
</section>

</body>
</html>
```